Property Report

8 page document, similar theme to our website (www.harbourandmeadows.com) and previous brochure (provided). All content provided. We want a professional looking document. We need ASAP. Thanks!

Industry/Entity Type

Property

Font styles to use
Serif
Sans Serif

Colors
ffc214
ffcf3e
fee18a
fff3d1

Requirements
Must have
• Page 1: Cover
Page 2: Content
Page 3: About Us
Page 4: Site Description
Page 5: Scheme
Page 6: Analysis
Page 7: Conclusion
Page 8: Contact Details

```html
<!DOCTYPE html>
<html lang="en">
<head>
<meta charset="utf-8">
<title>Harbour &amp; Meadows Commercial – Site Report Pages</title>
<link href="https://fonts.googleapis.com/css2?family=Montserrat:wght@400;500;600;700&family=Poppins:wght@600;700&display=swap" rel="stylesheet">
<style>
:root{
  --sky:#b9ecf6;
  --cream:#fff1cc;
  --orange:#f6a81c;
  --slate:#656b6e;
  --slate-dark:#3f4244;
  --ink:#1f1f1f;
  --white:#ffffff;
  --rule:#c9c2ad;
}
*{box-sizing:border-box;margin:0;padding:0}
html,body{width:857px;height:1200px;overflow:hidden;background:var(--sky)}
body{font-family:"Montserrat",sans-serif;color:var(--ink)}
.board{position:relative;width:1289px;height:1805px;transform:scale(.66486);transform-origin:0 0}
.page{position:absolute;width:368px;height:521px;background:var(--cream);overflow:hidden;box-shadow:3px 4px 8px rgba(0,0,0,.25)}
.col-1{left:51px}.col-2{left:449px}.col-3{left:847px}
.row-1{top:72px}.row-2{top:646px}.row-3{top:1228px}
.abs{position:absolute}
.page-no{position:absolute;right:11px;bottom:0;width:14px;height:25px;background:var(--orange);color:var(--white);font-size:8px;text-align:center;padding-top:4px}
.photo{position:absolute}
.photo-site{background:linear-gradient(180deg,#8fb3d6 0%,#a9c3dc 35%,#4a5a8a 55%,#7a7772 75%,#8e8d8a 100%)}
.photo-dark{background:linear-gradient(180deg,#4b4e51 0%,#5a5d60 45%,#474a4c 100%)}
.photo-city{background:linear-gradient(180deg,#3a3b3c 0%,#6c6f71 40%,#8e9193 60%,#3d3e3f 100%)}
.placeholder{position:absolute;background:var(--slate);color:#e9e9e9;font-size:20px;display:flex;align-items:center;justify-content:center}
.brand{position:absolute;color:var(--white);font-family:"Montserrat",sans-serif;font-weight:700;text-align:center;line-height:1}
.brand small{display:block;font-size:.5em;margin-top:4px}
h2.section-title{position:absolute;left:24px;top:44px;font-family:"Poppins",sans-serif;font-weight:700;font-size:18px}
.title-rule{position:absolute;left:24px;top:74px;width:150px;height:1px;background:var(--rule)}
.title-rule::before{content:"";position:absolute;left:0;top:-1px;width:45px;height:2px;background:var(--orange)}
.small-copy{font-size:6.2px;line-height:1.8}
.small-copy p+p{margin-top:8px}
/* cover */
.cover-brand-box{left:22px;top:0;width:133px;height:134px;background:var(--slate)}
.cover-badge{left:22px;top:385px;height:34px;padding:0 11px;background:var(--orange);color:var(--white);font-family:"Poppins",sans-serif;font-weight:700;font-size:22px;line-height:34px}
.cover-rule{left:22px;top:418px;width:324px;height:2px;background:var(--orange)}
.cover-address{left:23px;top:436px;font-size:12.5px;font-weight:500}
.cover-short-rule{left:23px;top:465px;width:87px;height:1.5px;background:var(--orange)}
.cover-client{left:23px;top:480px;font-size:9.5px}
/* contents */
.contents-panel{left:172px;top:250px;width:175px;height:271px;background:var(--cream);padding:25px 0 0 35px}
.contents-panel h2{font-family:"Poppins",sans-serif;font-size:17px;font-weight:700}
.contents-panel .rule{width:104px;height:1px;background:var(--rule);margin:10px 0 16px;position:relative}
.contents-panel .rule::before{content:"";position:absolute;left:0;top:-1px;width:45px;height:2px;background:var(--orange)}
.toc{list-style:none}
.toc li{display:flex;align-items:center;height:26.3px;font-size:9.5px}
.toc span{width:14px;height:14px;background:var(--orange);color:var(--white);font-size:8px;display:flex;align-items:center;justify-content:center;margin-right:10px}
/* info pages */
.page-white{background:var(--white)}
.accent-band{position:absolute;left:28px;width:312px;height:10px;background:var(--orange)}
.info-panel{position:absolute;left:28px;width:312px;background:var(--cream);text-align:center;padding:0 26px}
.info-panel h2{font-family:"Poppins",sans-serif;font-weight:700;font-size:18px}
.info-panel .mini-rule{width:44px;height:2px;background:var(--orange);margin:6px auto 0}
/* case studies */
.case-card{position:absolute;left:166px;width:177px;height:109px;background:var(--white);padding:12px 10px;font-size:7.2px;line-height:1.6}
.case-card strong{display:block;font-weight:700;margin-bottom:8px}
.case-card p{margin-top:3px}
/* table */
.valuation{position:absolute;left:23px;top:287px;width:325px;border-collapse:collapse;font-size:5.6px}
.valuation th{background:var(--orange);color:var(--white);height:20px;font-weight:500;font-size:7px}
.valuation th:first-child{background:var(--slate)}
.valuation td{height:24px;text-align:center;border-right:1px solid #ddd}
.valuation td:first-child{background:var(--slate);color:var(--white);font-size:7px}
.valuation tr:nth-child(odd) td:not(:first-child){background:#e8e8e8}
.valuation tr:nth-child(even) td:not(:first-child){background:var(--white)}
/* conclusion */
.benefits{list-style:none;font-size:6.5px;line-height:2.3}
.benefits li::before{content:"• ";color:var(--orange)}
.split{display:flex;margin-top:14px}
.split div{flex:1;padding:0 6px;font-size:6.3px;line-height:1.7}
.split div+div{border-left:1px solid var(--orange)}
.split h3{font-family:"Poppins",sans-serif;font-size:10.5px;font-weight:700}
/* contact */
.contact{position:absolute;left:20px;top:436px;width:330px;color:var(--white);font-size:8.2px;line-height:1.9}
.contact h3{font-family:"Poppins",sans-serif;font-size:11.5px;font-weight:600;margin-bottom:2px}
.contact .cols{display:flex;gap:40px}
.contact .item{display:flex;gap:6px}
.contact svg{flex:none;margin-top:3px}
</style>
</head>
<body>
<main class="board">

  <!-- Cover -->
  <section class="page col-1 row-1">
    <div class="photo photo-site" style="left:22px;top:33px;width:324px;height:385px" role="img" aria-label="Photo of the development site under construction with scaffolding beside a road"></div>
    <div class="abs cover-brand-box"></div>
    <div class="brand" style="left:22px;top:52px;width:133px;font-size:21px">Harbour &amp;<br>Meadows<small>Commercial</small></div>
    <div class="abs cover-badge">SITE REPORT</div>
    <div class="abs cover-rule"></div>
    <p class="abs cover-address">118 Linford Road, Westbrook KT9 2PL</p>
    <div class="abs cover-short-rule"></div>
    <p class="abs cover-client">On behalf of Ashdown Vale Group Limited.</p>
  </section>

  <!-- Contents -->
  <section class="page col-2 row-1">
    <div class="photo photo-dark" style="inset:0" role="img" aria-label="Dimmed photo of a brick apartment block"></div>
    <div class="brand" style="left:30px;top:40px;width:120px;font-size:22px">Harbour &amp;<br>Meadows<small>Commercial</small></div>
    <div class="abs" style="left:317px;top:224px;width:51px;height:52px;background:#dadcdd"></div>
    <div class="abs" style="left:145px;top:373px;width:27px;height:148px;background:#a8adb0"></div>
    <nav class="abs contents-panel">
      <h2>Contents</h2>
      <div class="rule"></div>
      <ul class="toc">
        <li><span>3</span>About Us</li>
        <li><span>4</span>Site Description</li>
        <li><span>5</span>Scheme</li>
        <li><span>6</span>Case Studies</li>
        <li><span>7</span>Analysis</li>
        <li><span>8</span>Conclusion</li>
        <li><span>9</span>Contact Details</li>
      </ul>
    </nav>
  </section>

  <!-- About Us -->
  <section class="page page-white col-3 row-1">
    <div class="photo photo-city" style="left:0;top:0;width:368px;height:265px" role="img" aria-label="Black and white photo of silhouettes at a glass window overlooking a city skyline"></div>
    <div class="brand" style="left:84px;top:80px;width:200px;font-size:30px">Harbour &amp;<br>Meadows<small>Commercial</small></div>
    <div class="accent-band" style="top:224px"></div>
    <div class="info-panel" style="top:234px;height:243px;padding-top:28px">
      <h2>About Us</h2>
      <div class="mini-rule"></div>
      <div class="small-copy" style="margin-top:22px">
        <p>Harbour &amp; Meadows Commercial specialise in the acquisition and disposal of development, investment and commercial property in London and the Home Counties. Our consultants advise on a wide range of property types and use classes and are experts in identifying ways in which property owners can maximise value.</p>
        <p style="margin-top:12px">Our considerable knowledge of the property market and creative approach to delivering maximum value, has enabled us to become one of the most active development and investment consultancies in London and the South East.</p>
      </div>
    </div>
    <div class="page-no">3</div>
  </section>

  <!-- Site Description -->
  <section class="page col-1 row-2">
    <h2 class="section-title">Site Description</h2>
    <div class="title-rule"></div>
    <div class="abs small-copy" style="left:23px;top:96px;width:145px">
      <p>Harbour and Meadows Commercial have been asked by Daniel Ashdown the representative for Ashdown Vale Group Limited to advise on the best disposal method to maximise value for their property.</p>
      <p>The existing property measures approximately 9,655 square feet internally with parking spaces.</p>
    </div>
    <div class="abs small-copy" style="left:190px;top:96px;width:150px">
      <p>The site was granted permitted development rights in 2016 to be converted into 11 flats and 11 parking spaces but this was no implemented.</p>
      <p>We understand that the vendors operate their business from the premises and the property has a designated use class of B1(a) Office/E Class.</p>
    </div>
    <div class="placeholder" style="left:25px;top:228px;width:318px;height:230px" role="img" aria-label="Photo of the existing site">image</div>
    <div class="page-no">4</div>
  </section>

  <!-- Scheme -->
  <section class="page col-2 row-2">
    <h2 class="section-title">Scheme</h2>
    <div class="title-rule"></div>
    <p class="abs small-copy" style="left:24px;top:94px;width:240px">We have taken advice form Linework Architects who have reviewed the site and have come up with a scheme for 30 residential units</p>
    <div class="placeholder" style="left:24px;top:133px;width:140px;height:194px" role="img" aria-label="Scheme drawing">image</div>
    <div class="placeholder" style="left:176px;top:133px;width:167px;height:90px" role="img" aria-label="Scheme elevation">image</div>
    <div class="placeholder" style="left:176px;top:237px;width:167px;height:90px" role="img" aria-label="Scheme floor plan">image</div>
    <div class="placeholder" style="left:24px;top:340px;width:319px;height:140px" role="img" aria-label="Scheme street view">image</div>
    <div class="page-no">5</div>
  </section>

  <!-- Case Studies -->
  <section class="page col-3 row-2">
    <h2 class="section-title">Case Studies</h2>
    <div class="title-rule"></div>
    <p class="abs" style="left:24px;top:98px;font-size:10px">Compares</p>
    <div class="placeholder" style="left:24px;top:127px;width:142px;height:109px" role="img" aria-label="Photo of comparable site one">image</div>
    <article class="case-card" style="top:127px">
      <strong>Riverside Homes Group - Elmfield Clinic, Station Road, Westbrook KT9 5AB</strong>
      <p>37 Residential Units</p><p>Price: £4,486,970 Per plot £121,000</p><p>August 2019</p>
    </article>
    <div class="placeholder" style="left:24px;top:249px;width:142px;height:109px" role="img" aria-label="Photo of comparable site two">image</div>
    <article class="case-card" style="top:249px;padding-top:10px">
      <strong style="margin-bottom:4px">Private Developer - Car Sales Show Rooms And Lock Ups Adjacent To Arterial Service Station, Ferry Road, Northam, London SW21 4DQ</strong>
      <p>32 Residential Flats</p><p>Price: £1,400,000 – Per Plot £44,000</p><p>August 2019</p>
    </article>
    <div class="placeholder" style="left:24px;top:371px;width:142px;height:109px" role="img" aria-label="Photo of comparable site three">image</div>
    <article class="case-card" style="top:371px">
      <strong>Beacon Housing - Land On The South Side Of Holloway Lane, London SW22 7EF</strong>
      <p>74 Residential Units</p><p>Price: £11,050,000 Per Plot £149,000</p><p>June 2019</p>
    </article>
    <div class="page-no">6</div>
  </section>

  <!-- Analysis -->
  <section class="page col-1 row-3">
    <h2 class="section-title">Analysis</h2>
    <div class="title-rule"></div>
    <p class="abs" style="left:23px;top:90px;font-size:11px;font-weight:500">Consented Site Valuation Variable</p>
    <p class="abs" style="left:23px;top:106px;font-size:6.3px">Please see below assumed land valuation upon delivery of planning permission.</p>
    <table class="valuation" style="top:130px">
      <tr><th></th><th>30</th><th>32</th><th>34</th><th>36</th><th>38</th><th>40</th><th>42</th></tr>
      <tr><td>£ 65,000</td><td>£ 1,950,000</td><td>£ 2,080,000</td><td>£ 2,210,000</td><td>£ 2,340,000</td><td>£ 2,470,000</td><td>£ 2,600,000</td><td>£ 2,730,000</td></tr>
      <tr><td>£ 75,000</td><td>£ 2,250,000</td><td>£ 2,400,000</td><td>£ 2,550,000</td><td>£ 2,700,000</td><td>£ 2,850,000</td><td>£ 3,000,000</td><td>£ 3,150,000</td></tr>
      <tr><td>£ 85,000</td><td>£ 2,550,000</td><td>£ 2,720,000</td><td>£ 2,890,000</td><td>£ 3,060,000</td><td>£ 3,230,000</td><td>£ 3,400,000</td><td>£ 3,400,000</td></tr>
      <tr><td>£ 95,000</td><td>£ 2,850,000</td><td>£ 3,040,000</td><td>£ 3,230,000</td><td>£ 3,420,000</td><td>£ 3,610,000</td><td>£ 3,800,000</td><td>£ 3,800,000</td></tr>
      <tr><td>£ 105,000</td><td>£ 3,150,000</td><td>£ 3,360,000</td><td>£ 3,570,000</td><td>£ 3,780,000</td><td>£ 3,990,000</td><td>£ 4,200,000</td><td>£ 4,200,000</td></tr>
    </table>
    <div class="placeholder" style="left:23px;top:290px;width:325px;height:175px" role="img" aria-label="Analysis chart or site photo">image</div>
    <div class="page-no">7</div>
  </section>

  <!-- Conclusion -->
  <section class="page page-white col-2 row-3">
    <div class="photo photo-city" style="left:0;top:0;width:368px;height:195px" role="img" aria-label="Black and white photo of silhouettes at a window above a city skyline"></div>
    <div class="accent-band" style="top:170px"></div>
    <div class="info-panel" style="top:180px;height:297px;padding-top:16px">
      <h2>Conclusion</h2>
      <p style="font-size:7.8px;line-height:1.7;margin-top:12px">Package Led Land Sale Involves selling the site to a Housing Association with a contractor already in place.</p>
      <h3 style="font-family:'Poppins',sans-serif;font-size:10.5px;margin-top:12px">Benefits:</h3>
      <ul class="benefits">
        <li>Housing Association has build cost certainty.</li>
        <li>No need to tender build.</li>
        <li>More interest from HA if builder in place.</li>
        <li>HA responds better to contractor.</li>
        <li>Contractor will identify potential issues coming from HA.</li>
        <li>No SDLT or CIL.</li>
      </ul>
      <div class="split">
        <div><h3>Private Sale</h3>Likely to be of interest to private market but beholden to market conditions and market appetite.</div>
        <div><h3>Alternative User</h3>Limited Experience in Private Rented Sector and income led purchasers as is a relatively new market.</div>
      </div>
    </div>
    <div class="page-no">8</div>
  </section>

  <!-- Contact Details -->
  <section class="page col-3 row-3">
    <div class="photo photo-city" style="inset:0" role="img" aria-label="Black and white photo of silhouettes in a glass tower overlooking a city"></div>
    <div class="brand" style="left:44px;top:188px;width:280px;font-size:42px">Harbour &amp;<br>Meadows<small>Commercial</small></div>
    <address class="contact" style="font-style:normal">
      <h3>Harbour &amp; Meadows Commercial</h3>
      <div class="cols">
        <div class="item">
          <svg width="7" height="9" viewBox="0 0 7 9"><path d="M3.5 0A3.5 3.5 0 0 0 0 3.5C0 6 3.5 9 3.5 9S7 6 7 3.5A3.5 3.5 0 0 0 3.5 0Zm0 5A1.5 1.5 0 1 1 3.5 2a1.5 1.5 0 0 1 0 3Z" fill="#f6a81c"/></svg>
          <div>Unit 4, 9 Marlow Road<br>London, SE21 6QT</div>
        </div>
        <div>
          <div class="item"><svg width="8" height="8" viewBox="0 0 8 8"><path d="M1.6 0 3 1.9 2.2 2.9a5 5 0 0 0 2.9 2.9l1-.8L8 6.4 7 8C3.2 7.8.2 4.8 0 1Z" fill="#f6a81c"/></svg>020 7946 0321</div>
          <div class="item"><svg width="9" height="7" viewBox="0 0 9 7"><rect width="9" height="7" rx="1" fill="#f6a81c"/><path d="M0 .5 4.5 4 9 .5" stroke="#3f4244" stroke-width=".8" fill="none"/></svg>info@harbourandmeadows.com</div>
        </div>
      </div>
    </address>
    <div class="page-no">9</div>
  </section>

</main>
</body>
</html>
```